Fifty Turning Pages

- Title: FIFTY TURNING PAGES
- Subtitle: 50 Years • 50 Songs • A Lifetime of Memories
- Content: 50 songs (year + artist) listed between 1976–2024 - see attached file for song listing
- Personal dedication: “For the woman who remembers life one song at a time. Happy 50th Birthday — January 2025. With love, Harold.”
- Final size: A2 (420 × 594 mm)
- Style: Elegant, music-themed, typography-led (minimal graphic elements like vinyl / soundwave / gold line accents).
- Deliverables: High-resolution A2 PDF (print-ready), plus source file (Canva/PSD/AI).
- Color preference: Matte palette (black/white/cream/gold accents).
- Target: Framed print quality poster.

```html
<!DOCTYPE html>
<html lang="en">
<head>
<meta charset="utf-8">
<title>Fifty Turning Pages</title>
<link href="https://fonts.googleapis.com/css2?family=Poppins:wght@800;900&family=Quicksand:wght@500;600&family=Dancing+Script:wght@700&family=Roboto+Condensed:wght@400&display=swap" rel="stylesheet">
<style>
  :root{
    --brown-deep:#4a3212;
    --brown:#6e5018;
    --gold:#a88f1c;
    --gold-bright:#c2aa2a;
    --cream:#f3dfc1;
    --white:#ffffff;
    --ink-shadow:rgba(0,0,0,.45);
  }
  *{margin:0;padding:0;box-sizing:border-box}
  html,body{width:840px;height:1200px;overflow:hidden}
  body{background:var(--brown-deep)}
  .poster{
    position:relative;width:840px;height:1200px;overflow:hidden;
    background:
      radial-gradient(ellipse 60% 45% at 85% 55%, var(--gold-bright) 0%, transparent 70%),
      radial-gradient(ellipse 70% 40% at 20% 20%, var(--brown) 0%, transparent 75%),
      linear-gradient(180deg, var(--brown) 0%, var(--gold) 45%, var(--gold) 62%, var(--brown) 85%, var(--brown-deep) 100%);
    color:var(--white);
  }
  .collage,.ribbons{position:absolute;left:0;top:0}
  .title{
    position:absolute;left:52px;top:414px;width:600px;
    font-family:"Poppins",sans-serif;font-weight:900;
    font-size:82px;letter-spacing:-3px;
    filter:drop-shadow(2px 3px 3px var(--ink-shadow));
  }
  .title-line{
    display:block;height:68px;line-height:68px;overflow:visible;
    background:linear-gradient(180deg,var(--cream) 0 50%,var(--white) 50% 100%);
    -webkit-background-clip:text;background-clip:text;color:transparent;
  }
  .subtitle{
    position:absolute;left:0;width:840px;top:636px;text-align:center;
    font-family:"Dancing Script",cursive;font-weight:700;font-size:40px;line-height:44px;
    text-shadow:1px 2px 3px var(--ink-shadow);
  }
  .timeline{position:absolute;left:0;top:0}
  .entry{position:absolute;width:78px;margin-left:-39px;text-align:center}
  .entry.wide{width:86px;margin-left:-43px}
  .entry .year{display:block;font-family:"Poppins",sans-serif;font-weight:800;font-size:13px;line-height:16px}
  .entry .artist{display:block;font-family:"Quicksand",sans-serif;font-weight:600;font-size:10px;line-height:14px}
  .dedication{position:absolute;left:0;width:840px;text-align:center;line-height:1}
  .dedication-note{top:1058px;font-family:"Roboto Condensed",sans-serif;font-size:28px}
  .dedication-greeting{top:1096px;font-family:"Poppins",sans-serif;font-weight:800;font-size:35px;letter-spacing:-.8px}
  .dedication-sign{top:1143px;font-family:"Roboto Condensed",sans-serif;font-size:30px}
</style>
</head>
<body>
<main class="poster">

  <svg class="ribbons" width="840" height="1200" viewBox="0 0 840 1200" role="img" aria-label="Flowing gold satin ribbons framing the poster">
    <defs>
      <linearGradient id="satin" x1="0" y1="0" x2="1" y2="1">
        <stop offset="0" stop-color="#d8c24a"/>
        <stop offset="1" stop-color="#8a7212"/>
      </linearGradient>
    </defs>
    <path d="M0 40 Q60 20 110 60 Q80 110 0 120 Z" fill="url(#satin)" opacity=".8"/>
    <path d="M560 0 Q650 30 760 10 Q820 30 840 60 L840 0 Z" fill="url(#satin)" opacity=".8"/>
    <path d="M0 930 Q60 900 80 960 Q60 1060 110 1200 L0 1200 Z" fill="url(#satin)" opacity=".75"/>
    <path d="M840 1100 Q790 1120 770 1160 Q760 1190 740 1200 L840 1200 Z" fill="url(#satin)" opacity=".75"/>
  </svg>

  <svg class="collage" width="840" height="650" viewBox="0 0 840 650" role="img" aria-label="Black and white photo collage of singers and music groups, with a studio microphone">
    <defs>
      <linearGradient id="photoTone" x1="0" y1="0" x2="0" y2="1">
        <stop offset="0" stop-color="#3a3a3a"/>
        <stop offset=".6" stop-color="#8a8a8a"/>
        <stop offset="1" stop-color="#cfcfcf" stop-opacity=".2"/>
      </linearGradient>
    </defs>
    <path d="M80 40 Q140 10 200 30 L380 20 L520 30 L640 10 Q720 20 770 60 L800 180 L790 260 L810 360 L800 470 L790 620 L690 640 L660 560 L620 400 L560 390 L440 385 L300 380 L160 400 L70 395 L60 300 L50 200 Z" fill="url(#photoTone)" opacity=".85"/>
  </svg>

  <h1 class="title">
    <span class="title-line">FIFTY</span>
    <span class="title-line">TURNING</span>
    <span class="title-line">PAGES</span>
  </h1>

  <p class="subtitle">50 Years • 50 Songs • A Lifetime Memories</p>

  <svg class="timeline" width="840" height="1200" viewBox="0 0 840 1200" aria-hidden="true">
    <g stroke="#ffffff" stroke-width="1.2">
      <line x1="106" y1="708" x2="754" y2="708"/>
      <line x1="106" y1="779" x2="754" y2="779"/>
      <line x1="106" y1="852" x2="754" y2="852"/>
      <line x1="106" y1="921" x2="754" y2="921"/>
      <line x1="106" y1="988" x2="679" y2="988"/>
    </g>
    <g fill="#ffffff">
      <circle cx="106" cy="708" r="5"/><circle cx="179" cy="708" r="5"/><circle cx="250" cy="708" r="5"/><circle cx="321" cy="708" r="5"/><circle cx="395" cy="708" r="5"/><circle cx="465" cy="708" r="5"/><circle cx="536" cy="708" r="5"/><circle cx="609" cy="708" r="5"/><circle cx="679" cy="708" r="5"/><circle cx="754" cy="708" r="5"/>
      <circle cx="106" cy="779" r="5"/><circle cx="179" cy="779" r="5"/><circle cx="250" cy="779" r="5"/><circle cx="321" cy="779" r="5"/><circle cx="395" cy="779" r="5"/><circle cx="465" cy="779" r="5"/><circle cx="536" cy="779" r="5"/><circle cx="609" cy="779" r="5"/><circle cx="679" cy="779" r="5"/><circle cx="754" cy="779" r="5"/>
      <circle cx="106" cy="852" r="5"/><circle cx="179" cy="852" r="5"/><circle cx="250" cy="852" r="5"/><circle cx="321" cy="852" r="5"/><circle cx="395" cy="852" r="5"/><circle cx="465" cy="852" r="5"/><circle cx="536" cy="852" r="5"/><circle cx="609" cy="852" r="5"/><circle cx="679" cy="852" r="5"/><circle cx="754" cy="852" r="5"/>
      <circle cx="106" cy="921" r="5"/><circle cx="179" cy="921" r="5"/><circle cx="250" cy="921" r="5"/><circle cx="321" cy="921" r="5"/><circle cx="395" cy="921" r="5"/><circle cx="465" cy="921" r="5"/><circle cx="536" cy="921" r="5"/><circle cx="609" cy="921" r="5"/><circle cx="679" cy="921" r="5"/><circle cx="754" cy="921" r="5"/>
      <circle cx="106" cy="988" r="5"/><circle cx="179" cy="988" r="5"/><circle cx="250" cy="988" r="5"/><circle cx="321" cy="988" r="5"/><circle cx="395" cy="988" r="5"/><circle cx="465" cy="988" r="5"/><circle cx="536" cy="988" r="5"/><circle cx="609" cy="988" r="5"/><circle cx="679" cy="988" r="5"/>
    </g>
  </svg>

  <section class="song-list">
    <div class="entry" style="left:106px;top:718px"><span class="year">1976</span><span class="artist">Opal<br>Fenwick</span></div>
    <div class="entry" style="left:179px;top:718px"><span class="year">1977</span><span class="artist">Raymond<br>Pruitt</span></div>
    <div class="entry" style="left:250px;top:718px"><span class="year">1978</span><span class="artist">Greta<br>Lindqvist</span></div>
    <div class="entry" style="left:321px;top:718px"><span class="year">1979</span><span class="artist">Thaddeus<br>Crane</span></div>
    <div class="entry" style="left:395px;top:718px"><span class="year">1980</span><span class="artist">Noreen<br>Ashby</span></div>
    <div class="entry" style="left:465px;top:718px"><span class="year">1981</span><span class="artist">Cornell<br>Whitby</span></div>
    <div class="entry" style="left:536px;top:718px"><span class="year">1982</span><span class="artist">Ellis<br>Barrow</span></div>
    <div class="entry" style="left:609px;top:718px"><span class="year">1983</span><span class="artist">August<br>Penrose</span></div>
    <div class="entry" style="left:679px;top:718px"><span class="year">1984</span><span class="artist">Tin<br>Kettle</span></div>
    <div class="entry" style="left:754px;top:718px"><span class="year">1985</span><span class="artist">Vanterpool</span></div>

    <div class="entry" style="left:106px;top:789px"><span class="year">1986</span><span class="artist">Priscilla<br>Dunmore</span></div>
    <div class="entry" style="left:179px;top:789px"><span class="year">1987</span><span class="artist">Halcyon</span></div>
    <div class="entry" style="left:250px;top:789px"><span class="year">1988</span><span class="artist">Tobias<br>Greer</span></div>
    <div class="entry" style="left:321px;top:789px"><span class="year">1989</span><span class="artist">Velvet Parade</span></div>
    <div class="entry" style="left:395px;top:789px"><span class="year">1990</span><span class="artist">Ashgrove<br>Five</span></div>
    <div class="entry" style="left:465px;top:789px"><span class="year">1991</span><span class="artist">Delphine<br>Okoro</span></div>
    <div class="entry" style="left:536px;top:789px"><span class="year">1992</span><span class="artist">Orchid</span></div>
    <div class="entry" style="left:609px;top:789px"><span class="year">1993</span><span class="artist">Silk Rain</span></div>
    <div class="entry" style="left:679px;top:789px"><span class="year">1994</span><span class="artist">Imani Frost</span></div>
    <div class="entry" style="left:754px;top:789px"><span class="year">1995</span><span class="artist">Rosalind K.<br>Pierce</span></div>

    <div class="entry" style="left:106px;top:862px"><span class="year">1996</span><span class="artist">Harborline</span></div>
    <div class="entry" style="left:179px;top:862px"><span class="year">1997</span><span class="artist">Nadia<br>Vereen</span></div>
    <div class="entry" style="left:250px;top:862px"><span class="year">1998</span><span class="artist">Simone<br>Castellan</span></div>
    <div class="entry" style="left:321px;top:862px"><span class="year">1999</span><span class="artist">Three<br>Lanterns</span></div>
    <div class="entry" style="left:395px;top:862px"><span class="year">2000</span><span class="artist">Lucien Moray</span></div>
    <div class="entry" style="left:465px;top:862px"><span class="year">2001</span><span class="artist">Ingrid<br>Tallis</span></div>
    <div class="entry" style="left:536px;top:862px"><span class="year">2002</span><span class="artist">Benji Rook</span></div>
    <div class="entry" style="left:609px;top:862px"><span class="year">2003</span><span class="artist">Celeste Amara</span></div>
    <div class="entry" style="left:679px;top:862px"><span class="year">2004</span><span class="artist">Marcus Dell</span></div>
    <div class="entry" style="left:754px;top:862px"><span class="year">2005</span><span class="artist">Oren<br>Fairweather</span></div>

    <div class="entry" style="left:106px;top:931px"><span class="year">2006</span><span class="artist">Tavi Lund</span></div>
    <div class="entry" style="left:179px;top:931px"><span class="year">2007</span><span class="artist">Juno Ashcroft</span></div>
    <div class="entry" style="left:250px;top:931px"><span class="year">2008</span><span class="artist">Little Pike</span></div>
    <div class="entry" style="left:321px;top:931px"><span class="year">2009</span><span class="artist">Stone Aldous<br>Ingrid Tallis</span></div>
    <div class="entry" style="left:395px;top:931px"><span class="year">2010</span><span class="artist">Cass Orwell</span></div>
    <div class="entry" style="left:465px;top:931px"><span class="year">2011</span><span class="artist">Mira<br>Holloway</span></div>
    <div class="entry" style="left:536px;top:931px"><span class="year">2012</span><span class="artist">Juno Ashcroft</span></div>
    <div class="entry" style="left:609px;top:931px"><span class="year">2013</span><span class="artist">Reid Calloway<br>Stone Aldous</span></div>
    <div class="entry" style="left:679px;top:931px"><span class="year">2014</span><span class="artist">Ferris<br>Oyelaran</span></div>
    <div class="entry" style="left:754px;top:931px"><span class="year">2015</span><span class="artist">The<br>Late Hours</span></div>

    <div class="entry wide" style="left:106px;top:998px"><span class="year">2016</span><span class="artist">Cass Orwell,<br>Zeke &amp; Lira</span></div>
    <div class="entry wide" style="left:179px;top:998px"><span class="year">2017</span><span class="artist">Emeric Vane<br>&amp; Noa</span></div>
    <div class="entry" style="left:250px;top:998px"><span class="year">2018</span><span class="artist">Dex Hollis<br>ft Grim</span></div>
    <div class="entry" style="left:321px;top:998px"><span class="year">2019</span><span class="artist">Keon Ambrose</span></div>
    <div class="entry wide" style="left:395px;top:998px"><span class="year">2020</span><span class="artist">Alden Crewe<br>ft Nia Soto</span></div>
    <div class="entry" style="left:465px;top:998px"><span class="year">2021</span><span class="artist">Rafael Dune</span></div>
    <div class="entry" style="left:536px;top:998px"><span class="year">2022</span><span class="artist">Vela</span></div>
    <div class="entry" style="left:609px;top:998px"><span class="year">2023</span><span class="artist">Zuri Okafor</span></div>
    <div class="entry wide" style="left:679px;top:998px"><span class="year">2024</span><span class="artist">Kasimir<br>Doyle ft Vela</span></div>
  </section>

  <p class="dedication dedication-note">For the woman who remembers life one song at a time</p>
  <p class="dedication dedication-greeting">Happy 50th Birthday January 2025</p>
  <p class="dedication dedication-sign">Love, Harold</p>

</main>
</body>
</html>
```